Small corporate website template design

I need a couple templates designed for a small corporate website. The corporate site reflects the existence of the parent company which will own various brands/services that have their own websites, so it will mainly be used to present who we are, what we do, what is happening (news/events), how to contact us, link off to our other brand/service sites, as well as post information for public relations, investors, and job opportunities.

The company name is Velmoranth LLC (www.velmoranth-example.com), and the name is representative of stratified layers of interconnected digital services. The corporate site is not expected to generate a bunch of fanfare - that honor will be reserved for the externally linked brand/service sites.

The provided logo may be manipulated in color, size, shape, positioning, etc. to get it to fit with the design, but should be integrated in some way.

What we are looking for is a home page layout as well as a template for an inner page whereby the navigation/logo, etc may be diminished to some extent for the inner pages. We are also interested in reusable elements such as dividers, content containers, etc. in order to represent the types of information described above that we would like to present as described above.

We are particularly interested in consistency of design elements, conservative use of color (including consideration of accessibility concerns), judicious use of whitespace in favor of simplified messaging, and something lending itself well to internationalization/translation.

Target Market(s)

Small business owners, entrepreneurs (B2B)

Number of Pages Required

2 page

Font styles to use
Sans Serif

Requirements
Must have
• See the attached PDF with the logo concept, color swatches, and comparative sites.

```html
<!DOCTYPE html>
<html lang="en">
<head>
<meta charset="utf-8">
<title>Velmoranth LLC — Home</title>
<link href="https://fonts.googleapis.com/css2?family=Lato:wght@400;700;900&family=Roboto:wght@400;500;700&display=swap" rel="stylesheet">
<style>
  :root{
    --orange:#f7941d;
    --orange-deep:#d86e0c;
    --navy:#0b2e63;
    --navy-dark:#082650;
    --ink:#333333;
    --muted:#8a8a8a;
    --white:#ffffff;
    --line:#d5d5d5;
  }
  *{box-sizing:border-box;margin:0;padding:0}
  html,body{width:1200px;height:2406px;overflow:hidden}
  body{position:relative;background:var(--white);font-family:"Lato",Arial,sans-serif;color:var(--ink)}
  .abs{position:absolute}

  /* Header */
  .top-strip{left:0;top:0;width:1200px;height:6px;background:var(--orange)}
  .site-header{left:0;top:6px;width:1200px;height:124px;background:var(--white)}
  .brand{left:77px;top:46px;display:flex;align-items:center;gap:10px;font-family:"Lato",sans-serif;font-weight:900;font-size:24px;color:var(--navy-dark)}
  .brand .dot{width:14px;height:14px;border-radius:50%;background:var(--orange)}
  .main-nav a{position:absolute;top:55px;font-family:"Roboto",sans-serif;font-size:19px;color:#555;text-decoration:none}
  .main-nav a.active{color:var(--orange);font-weight:500}
  .nav-pointer{left:272px;top:118px;width:0;height:0;border-left:12px solid transparent;border-right:12px solid transparent;border-bottom:12px solid var(--orange)}
  .phone-pill{left:804px;top:45px;width:166px;height:45px;border-radius:23px;background:var(--navy);color:var(--white);display:flex;align-items:center;justify-content:center;gap:10px;font-family:"Roboto",sans-serif;font-size:19px}
  .social-block{left:980px;top:6px;width:220px;height:124px;background:var(--orange-deep);display:flex;align-items:center;justify-content:center;gap:13px}
  .social-block span{width:30px;height:30px;border:2px solid var(--white);border-radius:50%}

  /* Hero */
  .hero{left:0;top:130px;width:1200px;height:573px;background:linear-gradient(180deg,#9aa3ab 0%,#c9ced2 40%,#7d8389 100%)}
  .hero-shade{left:0;top:130px;width:1200px;height:573px;background:rgba(20,25,35,.28)}
  .hero-title{left:0;top:305px;width:1200px;text-align:center;font-family:"Roboto",sans-serif;font-weight:700;font-size:46px;line-height:54px;color:var(--white);text-shadow:0 2px 6px rgba(0,0,0,.45)}
  .btn{display:flex;align-items:center;justify-content:center;font-family:"Lato",sans-serif;font-size:21px;color:var(--white);text-transform:uppercase}
  .btn-solid{left:407px;top:454px;width:187px;height:60px;background:var(--orange);border-radius:2px}
  .btn-ghost{left:605px;top:454px;width:186px;height:60px;border:2px solid var(--white);border-radius:2px}
  .slider-arrow{width:52px;height:52px;border-radius:50%;display:flex;align-items:center;justify-content:center}
  .slider-arrow.prev{left:51px;top:391px;background:#e9e9e9}
  .slider-arrow.next{left:1097px;top:391px;background:#333}

  /* About */
  .section-title{font-family:"Roboto",sans-serif;font-weight:700;font-size:36px;color:var(--navy)}
  .about-title{left:79px;top:765px}
  .about-rule{left:361px;top:796px;width:72px;height:1px;background:var(--line)}
  .about-text{left:79px;top:828px;width:665px;font-size:13.5px;line-height:25.5px;color:#555}
  .btn-read{left:77px;top:959px;width:156px;height:60px;background:var(--orange);border-radius:3px;box-shadow:0 3px 0 var(--orange-deep);font-size:21px}
  .about-visual{left:807px;top:770px;width:316px;height:252px;background:linear-gradient(160deg,#e07a10 0%,#f4a23b 35%,#3f6aa8 65%,#1c3e75 100%);clip-path:polygon(12% 0,88% 0,100% 18%,100% 78%,88% 100%,12% 100%,0 78%,0 18%)}

  /* Services */
  .services{left:0;top:1094px;width:1200px;height:489px;background:linear-gradient(120deg,#3b4a5e 0%,#6f7e90 50%,#9aa6b2 100%)}
  .services-title{left:0;top:1152px;width:1200px;text-align:center;color:var(--white)}
  .title-rule{height:1px}
  .rule-light{background:rgba(255,255,255,.7)}
  .rule-grey{background:var(--line)}
  .service-card{top:1293px;width:311px;height:216px;background:var(--white);box-shadow:4px 5px 8px rgba(0,0,0,.35);text-align:center}
  .service-card h3{position:absolute;left:0;top:64px;width:100%;font-family:"Roboto",sans-serif;font-weight:400;font-size:19px;color:var(--navy)}
  .service-card p{position:absolute;left:30px;top:100px;width:251px;font-size:14px;line-height:24px;color:#666}
  .service-card .more{position:absolute;left:0;top:167px;width:100%;display:flex;justify-content:center;align-items:center;gap:10px;font-family:"Roboto",sans-serif;font-weight:500;font-size:14px;color:var(--navy)}
  .service-icon{top:1240px;width:104px;height:104px;border-radius:50%;background:var(--white);display:flex;align-items:center;justify-content:center}
  .service-icon span{width:84px;height:84px;border-radius:50%;background:var(--orange);display:flex;align-items:center;justify-content:center}

  /* Blog */
  .blog-title{left:0;top:1641px;width:1200px;text-align:center}
  .blog-photo{top:1728px;width:250px;height:210px}
  .date-badge{top:1857px;width:62px;height:76px;display:flex;flex-direction:column;align-items:center;justify-content:center;font-family:"Roboto",sans-serif;line-height:1.1}
  .date-badge b{font-weight:400;font-size:28px}
  .date-badge small{font-size:17px}
  .badge-orange{background:var(--orange);color:var(--white)}
  .badge-white{background:var(--white);color:#1a8fd0}
  .post-title{top:1728px;width:230px;font-family:"Roboto",sans-serif;font-weight:700;font-size:16px;line-height:25px}
  .post-meta{top:1793px;display:flex;align-items:center;gap:10px;font-size:13px;color:#666}
  .post-excerpt{top:1834px;width:215px;font-size:13.5px;line-height:24.5px;color:#999}

  /* Footer */
  .site-footer{left:0;top:2010px;width:1200px;height:332px;background:var(--navy)}
  .footer-heading{top:2070px;font-family:"Roboto",sans-serif;font-weight:700;font-size:20px;color:var(--orange)}
  .footer-divider{top:2077px;width:1px;height:193px;background:rgba(255,255,255,.35)}
  .quick-links{left:80px;top:2122px;list-style:none;font-size:14.5px;line-height:29px;color:var(--white)}
  .contact-row{left:273px;display:flex;gap:12px;font-size:13.5px;line-height:21px;color:var(--white)}
  .contact-row svg{flex:none}
  .contact-email{font-size:12.5px;letter-spacing:-0.1px}
  .footer-map{left:521px;top:2072px;width:207px;height:207px;border:4px solid #e8e8e8;background:linear-gradient(135deg,#eef0ec 0%,#dfe3da 55%,#e9e4cf 100%)}
  .social-row{left:815px;display:flex;align-items:center;gap:14px;font-size:14.5px;color:var(--white)}
  .social-row span{width:30px;height:30px;border:2px solid var(--white);border-radius:50%}
  .footer-brand{left:958px;top:2140px;width:242px;text-align:center;font-family:"Lato",sans-serif;font-weight:900;font-size:32px;color:var(--orange)}
  .copyright-bar{left:0;top:2342px;width:1200px;height:64px;background:var(--orange);display:flex;align-items:center;justify-content:center;gap:8px;font-size:13.5px;color:var(--white)}
</style>
</head>
<body>

<!-- Header -->
<div class="abs top-strip"></div>
<header class="abs site-header"></header>
<div class="abs brand"><span class="dot"></span>Velmoranth</div>
<nav class="main-nav">
  <a class="active" href="#" style="left:260px">Home</a>
  <a href="#" style="left:366px">About</a>
  <a href="#" style="left:471px">Services</a>
  <a href="#" style="left:596px">Blog</a>
  <a href="#" style="left:688px">Contact</a>
</nav>
<div class="abs phone-pill">
  <svg width="20" height="20" viewBox="0 0 24 24"><path fill="#fff" d="M6.6 10.8a15.1 15.1 0 0 0 6.6 6.6l2.2-2.2a1 1 0 0 1 1-.25 11.4 11.4 0 0 0 3.6.57 1 1 0 0 1 1 1V20a1 1 0 0 1-1 1A17 17 0 0 1 3 4a1 1 0 0 1 1-1h3.5a1 1 0 0 1 1 1c0 1.25.2 2.45.57 3.57a1 1 0 0 1-.25 1z"/></svg>
  555-012-468
</div>
<div class="abs social-block"><span></span><span></span><span></span></div>
<div class="abs nav-pointer"></div>

<!-- Hero -->
<section class="abs hero" role="img" aria-label="Photo of a team meeting around a table in a bright office"></section>
<div class="abs hero-shade"></div>
<h1 class="abs hero-title">Adaptive Software Technology<br>for the Digital Revolution</h1>
<a class="abs btn btn-solid">Our Services</a>
<a class="abs btn btn-ghost">Contact Us</a>
<div class="abs slider-arrow prev"><svg width="16" height="18" viewBox="0 0 16 18"><path d="M12 2 4 9l8 7" fill="none" stroke="#f7941d" stroke-width="3"/></svg></div>
<div class="abs slider-arrow next"><svg width="16" height="18" viewBox="0 0 16 18"><path d="m4 2 8 7-8 7" fill="none" stroke="#f7941d" stroke-width="3"/></svg></div>

<!-- About -->
<h2 class="abs section-title about-title">About Company</h2>
<div class="abs about-rule"></div>
<p class="abs about-text">Lorem Ipsum is simply dummy text of the printing and typesetting industry. Lorem Ipsum has been the industry's standard dummy text ever since the 1500s, when an unknown printer took a galley of type and scrambled it to make a type specimen book. It has survived not only five centuries, but also the leap into electronic typesetting, remaining essentially unchanged.</p>
<a class="abs btn btn-read">Read More</a>
<div class="abs about-visual" role="img" aria-label="Illustrated hexagonal block showing office team photos on its sides"></div>

<!-- Services -->
<section class="abs services" role="img" aria-label="Photo of hands working on documents and a laptop, darkened"></section>
<h2 class="abs section-title services-title">Our Services</h2>
<div class="abs title-rule rule-light" style="left:396px;top:1176px;width:79px"></div>
<div class="abs title-rule rule-light" style="left:730px;top:1176px;width:75px"></div>

<article class="abs service-card" style="left:101px">
  <h3>Marketing Strategy</h3>
  <p>Lorem Ipsum is simply dummy text of the printing and typesetting industry.</p>
  <div class="more">READ MORE <svg width="30" height="10" viewBox="0 0 30 10"><path d="M0 5h27M22 1l5 4-5 4" fill="none" stroke="#0b2e63" stroke-width="2"/></svg></div>
</article>
<article class="abs service-card" style="left:444px">
  <h3>Digital Analytics</h3>
  <p>Lorem Ipsum is simply dummy text of the printing and typesetting industry.</p>
  <div class="more">READ MORE <svg width="30" height="10" viewBox="0 0 30 10"><path d="M0 5h27M22 1l5 4-5 4" fill="none" stroke="#0b2e63" stroke-width="2"/></svg></div>
</article>
<article class="abs service-card" style="left:788px">
  <h3>Management and Optimization</h3>
  <p>Lorem Ipsum is simply dummy text of the printing and typesetting industry.</p>
  <div class="more">READ MORE <svg width="30" height="10" viewBox="0 0 30 10"><path d="M0 5h27M22 1l5 4-5 4" fill="none" stroke="#0b2e63" stroke-width="2"/></svg></div>
</article>

<div class="abs service-icon" style="left:204px"><span>
  <svg width="44" height="40" viewBox="0 0 44 40"><g fill="#fff"><rect x="4" y="26" width="6" height="12"/><rect x="13" y="20" width="6" height="18"/><rect x="22" y="23" width="6" height="15"/><rect x="31" y="14" width="6" height="24"/></g><path d="M4 18 14 10l8 5 14-11" fill="none" stroke="#fff" stroke-width="2.5"/></svg>
</span></div>
<div class="abs service-icon" style="left:547px"><span>
  <svg width="46" height="42" viewBox="0 0 46 42"><rect x="3" y="3" width="40" height="26" fill="none" stroke="#fff" stroke-width="3"/><g fill="#fff"><rect x="10" y="17" width="4" height="8"/><rect x="17" y="12" width="4" height="13"/><rect x="24" y="15" width="4" height="10"/><rect x="31" y="9" width="4" height="16"/><rect x="21" y="29" width="4" height="7"/><rect x="13" y="36" width="20" height="3"/></g></svg>
</span></div>
<div class="abs service-icon" style="left:891px"><span>
  <svg width="44" height="44" viewBox="0 0 44 44"><g fill="none" stroke="#fff" stroke-width="3"><circle cx="26" cy="16" r="9"/><circle cx="14" cy="30" r="7"/></g><g stroke="#fff" stroke-width="4"><path d="M26 3v4M26 25v4M13 16h4M35 16h4M14 19v3M14 38v3M3 30h3M22 30h3"/></g><circle cx="26" cy="16" r="3" fill="#fff"/><circle cx="14" cy="30" r="2.5" fill="#fff"/></svg>
</span></div>

<!-- Blog -->
<h2 class="abs section-title blog-title">Recent Blog</h2>
<div class="abs title-rule rule-grey" style="left:400px;top:1665px;width:76px"></div>
<div class="abs title-rule rule-grey" style="left:768px;top:1665px;width:30px"></div>

<div class="abs blog-photo" style="left:79px;background:linear-gradient(135deg,#6b7d8e 0%,#a9b4bd 50%,#d8dcdf 100%)" role="img" aria-label="Photo of colleagues discussing around a laptop"></div>
<div class="abs date-badge badge-orange" style="left:260px"><b>28</b><small>Dec</small></div>
<h3 class="abs post-title" style="left:350px;color:var(--orange)">Lorem Ipsum printing and typesetting industry.</h3>
<div class="abs post-meta" style="left:350px">By Admin
  <svg width="20" height="16" viewBox="0 0 20 16"><path d="M10 15 2.5 8A4.3 4.3 0 0 1 10 3a4.3 4.3 0 0 1 7.5 5z" fill="none" stroke="#666" stroke-width="1.5"/></svg>200
  <svg width="28" height="16" viewBox="0 0 28 16"><path d="M12 3h12v8h-3l-3 3v-3h-6z" fill="none" stroke="#666" stroke-width="1.5"/><path d="M6 6h8v6H9l-3 2v-2H4V6z" fill="#666"/></svg>80
</div>
<p class="abs post-excerpt" style="left:350px">Lorem Ipsum is simply dummy text of the printing and text is typesetting industry. Lorem Ipsum has been the industry's</p>

<div class="abs blog-photo" style="left:616px;background:linear-gradient(135deg,#e9ece9 0%,#b9c0c2 50%,#7d8588 100%)" role="img" aria-label="Photo of two businessmen shaking hands by a window"></div>
<div class="abs date-badge badge-white" style="left:798px"><b>28</b><small>Dec</small></div>
<h3 class="abs post-title" style="left:887px;color:#222">Lorem Ipsum printing and typesetting industry.</h3>
<div class="abs post-meta" style="left:887px">By Admin
  <svg width="20" height="16" viewBox="0 0 20 16"><path d="M10 15 2.5 8A4.3 4.3 0 0 1 10 3a4.3 4.3 0 0 1 7.5 5z" fill="none" stroke="#666" stroke-width="1.5"/></svg>200
  <svg width="28" height="16" viewBox="0 0 28 16"><path d="M12 3h12v8h-3l-3 3v-3h-6z" fill="none" stroke="#666" stroke-width="1.5"/><path d="M6 6h8v6H9l-3 2v-2H4V6z" fill="#666"/></svg>80
</div>
<p class="abs post-excerpt" style="left:887px">Lorem Ipsum is simply dummy text of the printing and text is typesetting industry. Lorem Ipsum has been the industry's</p>

<!-- Footer -->
<footer class="abs site-footer"></footer>
<h4 class="abs footer-heading" style="left:80px">Quick Links</h4>
<ul class="abs quick-links"><li>Home</li><li>About</li><li>Services</li><li>News</li><li>Contact</li></ul>
<div class="abs footer-divider" style="left:229px"></div>

<h4 class="abs footer-heading" style="left:273px">Contact Us</h4>
<div class="abs contact-row" style="top:2122px">
  <svg width="20" height="22" viewBox="0 0 20 22"><path d="M10 2a6 6 0 0 0-6 6c0 4.5 6 11 6 11s6-6.5 6-11a6 6 0 0 0-6-6z" fill="none" stroke="#fff" stroke-width="2"/><circle cx="10" cy="8" r="2" fill="#fff"/><path d="M3 20h14" stroke="#fff" stroke-width="2"/></svg>
  <span>27 Mill Road, Eastbury,<br>Region 482019</span>
</div>
<div class="abs contact-row" style="top:2183px">
  <svg width="20" height="20" viewBox="0 0 24 24"><path fill="#fff" d="M6.6 10.8a15.1 15.1 0 0 0 6.6 6.6l2.2-2.2a1 1 0 0 1 1-.25 11.4 11.4 0 0 0 3.6.57 1 1 0 0 1 1 1V20a1 1 0 0 1-1 1A17 17 0 0 1 3 4a1 1 0 0 1 1-1h3.5a1 1 0 0 1 1 1c0 1.25.2 2.45.57 3.57a1 1 0 0 1-.25 1z"/></svg>
  <span>555-012-468</span>
</div>
<div class="abs contact-row" style="top:2223px">
  <svg width="20" height="16" viewBox="0 0 22 16"><rect x="1" y="1" width="20" height="14" fill="#fff"/><path d="m1 1 10 8 10-8" fill="none" stroke="#0b2e63" stroke-width="1.5"/></svg>
  <span class="contact-email">info@velmoranth-example.com</span>
</div>
<div class="abs footer-divider" style="left:489px"></div>

<div class="abs footer-map" role="img" aria-label="Street map showing the office location"></div>
<div class="abs footer-divider" style="left:770px"></div>

<h4 class="abs footer-heading" style="left:815px">Get Social</h4>
<div class="abs social-row" style="top:2123px"><span></span>Friendloop</div>
<div class="abs social-row" style="top:2175px"><span></span>Worklinker</div>
<div class="abs social-row" style="top:2227px"><span></span>Chirpline</div>
<div class="abs footer-divider" style="left:958px"></div>

<div class="abs footer-brand">Velmoranth</div>

<div class="abs copyright-bar">
  <svg width="14" height="14" viewBox="0 0 14 14"><circle cx="7" cy="7" r="6" fill="none" stroke="#fff" stroke-width="1.4"/><path d="M9 5.2A2.5 2.5 0 1 0 9 8.8" fill="none" stroke="#fff" stroke-width="1.4"/></svg>
  <span><b>Velmoranth</b> - 2018. All Rights Reserved</span>
</div>

</body>
</html>
```